Automotive Parts Company Business Card/Logo Design

We need a logo/business card for a new automotive parts and accessories company which is based in Barbados. The company will only have an online presence and this will reduce our overheads and allow us to pass potential savings to our customers.

We will offer most automotive parts which include, but are not limited to, accessories, exterior, interior, body parts.

We want to appeal to a very wide audience and we're looking for a modern, clean and bold design to make the company seem very professional. Our logo and facebook page will be our only customer facing items. So it is essential that these are done correctly.

The design should really communicate that we can provide premium car parts at affordable prices for all types of cars e.g. European and Japanese.

We will stock items and also source hard to get and unique pieces. We aim to not just be another shop that sells parts. But we want to work with our customers to achieve their car goals.

The company name is GearNest and our slogan is Quality Parts At Affordable Prices.
The design should be very modern, clean and bold.

I've included examples of some of the business cards I like as well as images of car products.
Updates

Dear Designers,

I've uploaded some samples of some business card/logo designs I like. Please have a look at the project brief. Just to reiterate, I am looking for a clean, modern design.

Thanks,

Rohan

Dear Designers,

Please note the Apr 14th deadline is soon approaching.

Also note the business card is double-sided.

I look forward to working with you.

Thanks,

Rohan

Target Market(s)

20 - 30 (young professionals, younger generation with disposible income) and then then all other markets

Industry/Entity Type

Automotive

Contact Information for Business Card

Rohan Mehtabrooke
GearNest
Quality Parts At Affordable Prices
https://www.example-social.test/gearnestbb
246-555-0192
gearnestbb@mailbox-demo.test

```html
<!DOCTYPE html>
<html lang="en">
<head>
<meta charset="utf-8">
<title>GearNest – Business Card</title>
<link rel="stylesheet" href="https://fonts.googleapis.com/css2?family=Alfa+Slab+One&family=Exo+2:wght@300&family=Zilla+Slab:ital,wght@1,700&display=swap">
<style>
  :root {
    --card-bg: #1a1a1a;
    --name-grey: #b9c1c6;
    --contact-text: #d8d8d8;
    --icon-pink: #e8345a;
    --brand-blue: #3aaee6;
    --brand-blue-light: #5cc4f2;
    --silver-light: #f2f2f2;
    --silver-dark: #6e6e6e;
  }
  html, body {
    margin: 0;
    padding: 0;
    width: 1200px;
    height: 741px;
    overflow: hidden;
    background: var(--card-bg);
  }
  .card {
    position: relative;
    width: 1200px;
    height: 741px;
    background: var(--card-bg);
    overflow: hidden;
  }
  .holder-name {
    position: absolute;
    left: 78px;
    top: 56px;
    margin: 0;
    font-family: "Zilla Slab", Georgia, serif;
    font-style: italic;
    font-weight: 700;
    font-size: 54px;
    letter-spacing: 2px;
    color: var(--name-grey);
  }
  .contact-list {
    position: absolute;
    left: 74px;
    top: 152px;
    margin: 0;
    padding: 0;
    list-style: none;
  }
  .contact-item {
    display: flex;
    align-items: center;
    height: 55px;
    font-family: "Exo 2", Arial, sans-serif;
    font-weight: 300;
    font-size: 25px;
    letter-spacing: 2px;
    color: var(--contact-text);
  }
  .contact-icon {
    width: 30px;
    height: 30px;
    margin-right: 24px;
    flex: none;
  }
  .brand-mark {
    position: absolute;
    left: 800px;
    top: 110px;
    width: 320px;
    height: 240px;
    display: flex;
    align-items: center;
    justify-content: center;
    gap: 16px;
  }
  .brand-mark-dot {
    width: 44px;
    height: 44px;
    border-radius: 50%;
    background: var(--brand-blue);
  }
  .brand-mark-name {
    font-family: "Alfa Slab One", Georgia, serif;
    font-size: 46px;
    color: var(--brand-blue);
  }
  .ornament {
    position: absolute;
    left: 62px;
    top: 370px;
    width: 290px;
    height: 290px;
    border-radius: 50%;
    background: radial-gradient(circle, var(--silver-light) 0%, #bdbdbd 35%, var(--silver-dark) 55%, rgba(26,26,26,0) 72%);
  }
  .brand-name {
    position: absolute;
    left: 446px;
    top: 380px;
    margin: 0;
    font-family: "Alfa Slab One", Georgia, serif;
    font-weight: 400;
    font-size: 104px;
    line-height: 1;
    color: var(--brand-blue-light);
  }
  .slogan-main {
    position: absolute;
    left: 412px;
    top: 518px;
    margin: 0;
    font-family: "Alfa Slab One", Georgia, serif;
    font-size: 82px;
    line-height: 1;
    color: var(--brand-blue);
    transform: skewX(-12deg);
    transform-origin: left bottom;
  }
  .slogan-sub {
    position: absolute;
    left: 352px;
    top: 632px;
    margin: 0;
    font-family: "Alfa Slab One", Georgia, serif;
    font-size: 46px;
    line-height: 1;
    letter-spacing: 5px;
    color: var(--brand-blue);
    transform: skewX(-12deg);
    transform-origin: left bottom;
  }
</style>
</head>
<body>
<main class="card">
  <h1 class="holder-name">Rohan Mehtabrooke</h1>

  <ul class="contact-list">
    <li class="contact-item">
      <svg class="contact-icon" viewBox="0 0 30 30" aria-hidden="true">
        <rect x="4" y="4" width="22" height="22" rx="3" fill="var(--icon-pink)"/>
      </svg>
      www.example-social.test/gearnestbb
    </li>
    <li class="contact-item">
      <svg class="contact-icon" viewBox="0 0 30 30" aria-hidden="true">
        <path d="M8 4c2 0 3 4 4 6s-2 3-2 4 3 6 5 7 2-2 4-2 5 2 5 4-3 4-5 3C11 24 6 16 6 8c0-2 1-4 2-4z" fill="var(--icon-pink)"/>
      </svg>
      246-555-0192
    </li>
    <li class="contact-item">
      <svg class="contact-icon" viewBox="0 0 30 30" aria-hidden="true">
        <rect x="3" y="8" width="24" height="15" fill="var(--icon-pink)"/>
        <path d="M3 8l12 9 12-9" fill="none" stroke="var(--card-bg)" stroke-width="2"/>
      </svg>
      gearnestbb@mailbox-demo.test
    </li>
  </ul>

  <div class="brand-mark">
    <span class="brand-mark-dot"></span>
    <span class="brand-mark-name">GearNest</span>
  </div>

  <div class="ornament" role="img" aria-label="Silver diamond starburst ornament"></div>

  <h2 class="brand-name">GearNest</h2>
  <p class="slogan-main">Quality Parts</p>
  <p class="slogan-sub">At affordable prices</p>
</main>
</body>
</html>
```